Brochure for financial planning firm

I need a brochure designed that will be folded into three panels idealy. I will provide the copy, logo, and some of the pictures.

Our primary business is finding investors for large-scale real estate developments.

Some of the pictures will have to come from outside this website given the file sizes. Please click the following link to download pictures of projects we have raised money for:

https://files.tarnuvex.net/share/7QmW2rLp94ZxKdTbYhVcNs3EaUfJ8gGo?view=open

Target Market(s)

People Ages 30 to 75. That are unsatisfied with their retirement investments

Industry/Entity Type

Financial

Requirements
Must have
• Addition to copy:
• To recieve information on our latest investments visit www.cloverpathsavings.ca
• Contact info:
• Tarrowby Wealth Management Inc.
• 4 Pellam Rd. W.
• Suite K300
• Hamilton, ON K2R 7T5
• Office: (905) 463-2918
• www.tarrowbywm.com
• The brochure must have somewhere printed on it near our contact info: RBQT Lic # 40963

```html
<!DOCTYPE html>
<html lang="en">
<head>
<meta charset="utf-8">
<title>Tarrowby Wealth Management – Tri-fold Brochure</title>
<link href="https://fonts.googleapis.com/css2?family=Montserrat:wght@400;600;700&family=Open+Sans:ital,wght@0,400;0,600;1,400&display=swap" rel="stylesheet">
<style>
  :root{
    --teal:#2ad3bb;
    --teal-deep:#1fb9a3;
    --ink:#2a2a2e;
    --plum:#3a3545;
    --text:#3b3b3b;
    --paper:#ffffff;
    --bg:#d9d9d9;
  }
  *{box-sizing:border-box;margin:0;padding:0}
  html,body{width:1200px;height:1200px;overflow:hidden;background:var(--bg)}
  body{position:relative;font-family:"Open Sans",sans-serif;color:var(--text)}
  .sheet{position:absolute;left:190px;width:820px;height:565px;background:var(--paper);display:grid;grid-template-columns:repeat(3,1fr);box-shadow:0 6px 18px rgba(0,0,0,.18)}
  .sheet--outside{top:20px}
  .sheet--inside{top:612px}
  .panel{position:relative;overflow:hidden;height:100%}
  .panel + .panel{border-left:1px solid #eee}
  .photo{position:absolute;left:0;width:100%}
  .wave{position:absolute;left:0;width:100%;display:block}
  .stripe{position:absolute;left:0;width:100%}
  .stripe--dark{background:var(--ink);height:9px;bottom:24px}
  .stripe--grey{background:#cfcfcf;height:5px;bottom:36px}
  .heading{font-family:"Montserrat",sans-serif;color:var(--teal);font-weight:600}
  p{font-size:8.3px;line-height:1.45}
  .accent{color:var(--teal);font-weight:600}

  /* outside – left */
  .promo .photo{top:0;height:300px;background:linear-gradient(160deg,#5d8fc4 0%,#9cc0dd 35%,#e8c8a0 70%,#b86b3e 100%)}
  .promo .wave{top:268px}
  .promo-copy{position:absolute;top:338px;left:22px;right:22px}
  .promo-copy .heading{font-size:12.5px;line-height:1.25;margin-bottom:14px}
  .promo-copy .lead{font-family:"Montserrat",sans-serif;font-weight:700;font-size:11px;color:var(--ink);line-height:1.35;margin-bottom:12px}
  .promo-copy p{text-align:justify}
  .promo-copy p.lead{text-align:left}

  /* outside – middle */
  .about-copy{position:absolute;top:26px;left:22px;right:22px}
  .about-copy .heading{font-size:12px;margin-bottom:8px}
  .about-copy p{margin-bottom:9px;text-align:justify}
  .contact .wave{top:288px}
  .contact-block{position:absolute;top:364px;left:18px;right:18px;text-align:center;color:#fff;font-family:"Montserrat",sans-serif}
  .contact-block address{font-style:normal;font-size:10.5px;line-height:1.45}
  .contact-block .licence{margin-top:6px;font-size:9px;font-weight:600}
  .contact-block .updates{margin-top:8px;font-size:8px;line-height:1.4}
  .contact-block .site{display:block;margin-top:10px;font-size:9px;font-weight:600}
  .contact .stripe--base{bottom:0;height:20px;background:var(--teal-deep)}

  /* outside – cover */
  .cover .masthead{position:absolute;top:0;left:0;width:100%;height:130px;background:var(--plum);display:flex;align-items:center;justify-content:center;gap:8px}
  .brand{font-family:"Montserrat",sans-serif;font-weight:600;font-size:20px;letter-spacing:3px;color:var(--teal)}
  .brand-mark{width:12px;height:12px;background:var(--teal)}
  .cover .photo{top:130px;height:220px;background:linear-gradient(180deg,#4a4a55 0%,#8d5a4a 45%,#b7a79a 75%,#6f8b4d 100%)}
  .cover .wave{top:318px}
  .cover-title{position:absolute;top:372px;left:28px;right:20px;font-family:"Montserrat",sans-serif;font-weight:700;font-size:22px;line-height:1.1;color:var(--ink)}
  .cover-title span{color:var(--teal);display:block;font-size:25px}
  .cover-title em{font-style:normal;display:block;font-size:25px}
  .cover .site{position:absolute;top:470px;right:22px;font-size:8px;font-family:"Montserrat",sans-serif;color:var(--ink)}

  /* inside – left */
  .reasons-copy{position:absolute;top:22px;left:24px;right:22px}
  .reasons-copy > p{font-style:italic;margin-bottom:12px}
  .reason{display:flex;gap:9px;margin-bottom:12px}
  .reason-num{flex:0 0 14px;height:14px;background:var(--teal);color:#fff;font-size:8px;font-weight:700;display:flex;align-items:center;justify-content:center;font-family:"Montserrat",sans-serif}
  .reason p{font-style:italic;text-align:justify}
  .reasons .wave{top:420px}
  .call-band{position:absolute;left:0;bottom:20px;width:100%;height:78px;background:var(--ink);color:#fff;padding:18px 0 0 34px;font-family:"Montserrat",sans-serif}
  .call-band .phone{color:var(--teal);font-size:14px;font-weight:600}
  .call-band .site{font-size:10px;margin-top:4px}
  .reasons .stripe--base{bottom:6px;height:8px;background:var(--teal)}

  /* inside – middle */
  .gallery .photo--top{top:0;height:300px;background:linear-gradient(180deg,#3f8fd8 0%,#8cc3ef 55%,#3c4a5a 100%)}
  .gallery .photo--bottom{bottom:0;height:175px;background:linear-gradient(180deg,#c9d7e2 0%,#7b6f6a 55%,#4f5a50 100%)}
  .gallery .wave{top:250px}
  .seal{position:absolute;top:248px;left:50%;transform:translateX(-50%);width:120px;height:120px;border-radius:50%;background:var(--ink);border:4px solid #fff;display:flex;align-items:center;justify-content:center}
  .seal .brand{font-size:15px;letter-spacing:2px}

  /* inside – right */
  .testimonials{position:absolute;top:20px;left:20px;right:20px}
  .testimonials .heading{font-size:11px;margin-bottom:4px}
  .quote{margin-bottom:8px}
  .quote p{font-style:italic;font-size:7.6px;line-height:1.4;text-align:justify}
  .quote cite{display:block;font-style:italic;font-size:7.6px;color:var(--teal);font-weight:600;margin-top:2px}
  .quote cite.plain{color:var(--ink)}
  .testimonials-base{position:absolute;left:0;bottom:14px;width:100%;height:9px;background:var(--teal)}
</style>
</head>
<body>

<section class="sheet sheet--outside" aria-label="Brochure outside">
  <article class="panel promo">
    <div class="photo" role="img" aria-label="Photo of a glass residential tower at sunset"></div>
    <svg class="wave" width="274" height="70" viewBox="0 0 274 70" preserveAspectRatio="none">
      <path d="M0 40 Q137 0 274 20 L274 70 L0 70Z" fill="#fff"/>
      <path d="M0 30 Q137 -8 274 10 L274 22 Q137 4 0 44Z" fill="var(--teal)"/>
    </svg>
    <div class="promo-copy">
      <h2 class="heading">Tired of investing in the stock market or the latest mutual fund?</h2>
      <p class="lead">We will help you finally make predictable, stable returns!</p>
      <p>If you have ever looked at your RRSP statement and wondered if there was something other than the stocks, bonds or mutual funds your banker or financial advisor have told you are your best choices to grow your investments, well…there are. They are <span class="accent">SYNDICATED MORTGAGES!</span></p>
    </div>
    <div class="stripe stripe--grey"></div>
    <div class="stripe stripe--dark"></div>
  </article>

  <article class="panel contact">
    <div class="about-copy">
      <h2 class="heading">Syndicated Mortgages</h2>
      <p>The simplest way to describe a syndicated mortgage is that it is a mortgage where two or more people loan their money in the form of one mortgage to another party.</p>
      <p>As a syndicated mortgage investor you become the bank! In other words, when you invest in a syndicated mortgage offered by Tarrowby Wealth Management you are lending your money to a reputable real estate developer for a set interest rate.</p>
      <p>You might be thinking that lending mortgages are only for people with really deep pockets but in fact, if you have even $25,000 sitting in an account a mortgage investment is something you could take advantage of. RRSP, TFSA, RRIF, LIRA's, and LIF's are only some of the account types that are eligible for syndicated mortgage investments.</p>
    </div>
    <svg class="wave" width="274" height="277" viewBox="0 0 274 277" preserveAspectRatio="none">
      <path d="M0 10 Q137 -6 274 40 L274 277 L0 277Z" fill="var(--teal)"/>
    </svg>
    <div class="contact-block">
      <address>Tarrowby Wealth Management Inc.<br>4 Pellam Rd. W.<br>Ground Floor, Suite K300<br>Hamilton, ON K2R 7T5<br>Office: (905) 463-2918<br>Fax: 1-866-463-0271</address>
      <p class="licence">RBQT Lic # 40963</p>
      <p class="updates">To receive information on our latest investments visit www.cloverpathsavings.ca</p>
      <span class="site">www.tarrowbywm.com</span>
    </div>
    <div class="stripe stripe--base"></div>
  </article>

  <article class="panel cover">
    <div class="masthead"><span class="brand-mark"></span><span class="brand">TARROWBY</span></div>
    <div class="photo" role="img" aria-label="Photo of a brick mid-rise condominium building"></div>
    <svg class="wave" width="274" height="50" viewBox="0 0 274 50" preserveAspectRatio="none">
      <path d="M0 0 Q137 40 274 10 L274 50 L0 50Z" fill="#fff"/>
      <path d="M0 0 Q137 40 274 10 L274 16 Q137 48 0 8Z" fill="var(--teal)"/>
    </svg>
    <h1 class="cover-title">USE YOUR RRSP<span>TO INVEST IN</span><em>REAL ESTATE</em></h1>
    <span class="site">www.tarrowbywm.com</span>
    <div class="stripe stripe--grey"></div>
    <div class="stripe stripe--dark"></div>
  </article>
</section>

<section class="sheet sheet--inside" aria-label="Brochure inside">
  <article class="panel reasons">
    <div class="reasons-copy">
      <p>There are many reasons why banks use mortgages as their preferred investments; here are just a few of those reasons and why you might want to think about adding a syndicated mortgage investment to your portfolio.</p>
      <div class="reason"><span class="reason-num">1</span><p>Security of principle. Your investment is registered against physical real estate at the Land Registry Office. This doesn't mean it's a guaranteed investment, but it definitely reduces the risk of loss the way no stock can.</p></div>
      <div class="reason"><span class="reason-num">2</span><p>A predictable rate of return. With a syndicated mortgage investment you know exactly what you are entitled to earn. The rate of interest is written right into your contract, not left to the ups and downs of the stock market.</p></div>
      <div class="reason"><span class="reason-num">3</span><p>Term investment periods. A syndicated mortgage investment can range between a few months to about five years, depending on the project.</p></div>
      <p>"Mortgage investments are quickly changing retirement portfolios. People are tired of not having control over their money. As a financial planner, mortgage investments give my clients a stable position to plan their financial lives." – Daniel Ferreira, Tarrowby Wealth Management.</p>
    </div>
    <svg class="wave" width="274" height="50" viewBox="0 0 274 50" preserveAspectRatio="none">
      <path d="M0 10 Q137 -4 274 30 L274 50 L0 50Z" fill="var(--teal)"/>
    </svg>
    <div class="call-band">
      <div class="phone">Call: (905) 463-2918</div>
      <div class="site">www.tarrowbywm.com</div>
    </div>
    <div class="stripe stripe--base"></div>
  </article>

  <article class="panel gallery">
    <div class="photo photo--top" role="img" aria-label="Photo of high-rise condominium towers against a blue sky"></div>
    <svg class="wave" width="274" height="150" viewBox="0 0 274 150" preserveAspectRatio="none">
      <path d="M0 30 Q100 70 274 20 L274 120 Q140 150 0 110Z" fill="var(--teal)"/>
      <path d="M0 30 Q100 70 274 20 L274 32 Q100 82 0 44Z" fill="#fff"/>
    </svg>
    <div class="photo photo--bottom" role="img" aria-label="Photo of a mid-rise residential development"></div>
    <div class="seal"><span class="brand">TARROWBY</span></div>
  </article>

  <article class="panel">
    <div class="testimonials">
      <h2 class="heading">Testimonials</h2>
      <div class="quote"><p>My husband and I had been looking for an alternative to investing in mutual funds and the stock market for a while. The unpredictability of our mutual funds was something we were sick and tired of. When we were introduced to the syndicated mortgage investments offered by Tarrowby Wealth Management, I thought the rate of return was too good to be true. Now we can sleep at night.</p><cite>Marta Velloni, Client</cite></div>
      <div class="quote"><p>My husband and I had always thought about investing from the time we got married but didn't know where to start. Daniel took the time to meet with us, he helped organize our current assets and then helped us to focus on our future needs and goals. I would definitely recommend Daniel to any of my family or friends.</p><cite>Renata Osborne, CA</cite></div>
      <div class="quote"><p>I would recommend Tarrowby Wealth Management (TWM) to anyone looking for professional financial advice regarding real estate investment strategy and financial planning. The TWM team is reliable, trustworthy, and focused on helping their clients achieve their financial goals.</p><cite>Peter Linholm,</cite><cite class="plain">Winner of the 2017 Rising Star award by Northern Property Investor Magazine</cite></div>
      <div class="quote"><p>When you are looking to expand your investment and real estate portfolio, Tarrowby Wealth Management Inc. is a true asset. I have gotten to know Daniel Ferreira over the years and he always demonstrates a keen knowledge and creative edge.</p><cite class="plain">Owen Marchetti, Professional Real Estate Investor</cite></div>
    </div>
    <div class="testimonials-base"></div>
  </article>
</section>

</body>
</html>
```